ZORM Design tag

Looking to design a tag for our new hat & glove brand ZORM Design. These are winter hats & gloves. Long story short these are lower cost/retail items but I'm trying to convey higher quality goods through a nice tag. I’ve attached a tag of another brand we have to give you a general idea of what I’d be looking for- but again for our new brand ZORM Design.
I’m thinking we can do one general design- and then do it in 4 different color schemes: First one mimicking the attachment’s colors for ladies items- so a few different shades of pink. Then 2nd color scheme a darker more masculine color tone for mens or unisex items- maybe blue/dark blue, and then a 3rd color scheme for kids items that is more vibrant/kid like colors. Last one red & green for some Christmas items we do.
A few things:
• Trying to make the tags look classy as possible
• The tag will need to measure 2.25” high x 2” wide. The top little bit would have to be space left blank for a hole punch- just like on the attached sample tag. But again the tags designed would need to be 2.25" tall x 2" wide so not the same shape as the sample tag.
• For item name you can just put “Knit Hat” for the generic tag item name (in place of what says on the same “Chenille Slipper Bootie”). Please try to keep the writing a nice font similar to what is on this tag- again trying to have a classy tag look
• On the bottom center (In place of Made in China) it would just need to say “One Size” in standard font
Hope this helps & thank you
People buying winter hats & gloves
Retail- winter hats & gloves

```html
<!DOCTYPE html>
<html lang="en">
<head>
<meta charset="utf-8">
<title>ZORM Design – Knit Hat Tags</title>
<link href="https://fonts.googleapis.com/css2?family=Oswald:wght@500&family=Sacramento&display=swap" rel="stylesheet">
<style>
  :root {
    --canvas-bg: #ecebe8;
    --tag-shadow: rgba(0, 0, 0, 0.18);
    --script-white: #ffffff;

    --holiday-base: #0e7a3c;
    --holiday-band: #e5262c;
    --holiday-ink: #0a4f27;

    --kids-base: #fbf59c;
    --kids-band: #fde31c;
    --kids-ink: #e0a800;

    --mens-base: #22b9ee;
    --mens-band: #1590c9;
    --mens-ink: #163a6a;

    --ladies-base: #e9a9cd;
    --ladies-band: #c48dc2;
    --ladies-ink: #d5529a;
  }

  * { box-sizing: border-box; margin: 0; padding: 0; }

  html, body {
    width: 1014px;
    height: 1200px;
    overflow: hidden;
    background: var(--canvas-bg);
  }

  .tag-sheet {
    width: 1014px;
    height: 1200px;
    display: grid;
    grid-template-columns: repeat(2, 420px);
    grid-template-rows: repeat(2, 472px);
    gap: 60px;
    justify-content: center;
    align-content: center;
  }

  .tag {
    position: relative;
    width: 420px;
    height: 472px;
    overflow: hidden;
    background: var(--base);
    box-shadow: 0 6px 18px var(--tag-shadow);
  }

  .tag--holiday { --base: var(--holiday-base); --band: var(--holiday-band); --ink: var(--holiday-ink); --brand-color: #ffffff; }
  .tag--kids    { --base: var(--kids-base);    --band: var(--kids-band);    --ink: var(--kids-ink);    --brand-color: #d49a00; }
  .tag--mens    { --base: var(--mens-base);    --band: var(--mens-band);    --ink: var(--mens-ink);    --brand-color: #163a6a; }
  .tag--ladies  { --base: var(--ladies-base);  --band: var(--ladies-band);  --ink: var(--ladies-ink);  --brand-color: #c23f88; }

  .tag__band {
    position: absolute;
    inset: 0;
    width: 100%;
    height: 100%;
  }

  .tag__band polygon { fill: var(--band); }

  .brand {
    position: absolute;
    top: 92px;
    left: 74px;
    display: flex;
    align-items: center;
    gap: 12px;
  }

  .brand__square {
    width: 26px;
    height: 26px;
    background: var(--ink);
  }

  .brand__name {
    font-family: "Oswald", sans-serif;
    font-weight: 500;
    font-size: 50px;
    line-height: 1;
    letter-spacing: 0.5px;
    text-transform: uppercase;
    color: var(--brand-color);
  }

  .item-name {
    position: absolute;
    top: 168px;
    left: 150px;
    font-family: "Sacramento", cursive;
    font-size: 96px;
    line-height: 0.8;
    color: var(--script-white);
    -webkit-text-stroke: 1.2px var(--ink);
  }

  .item-name span { display: block; }
  .item-name span + span { margin-top: 10px; }

  .size {
    position: absolute;
    bottom: 20px;
    left: 0;
    right: 0;
    text-align: center;
    font-family: "Oswald", sans-serif;
    font-weight: 500;
    font-size: 14px;
    letter-spacing: 0.5px;
    text-transform: uppercase;
    color: var(--script-white);
  }
</style>
</head>
<body>
  <main class="tag-sheet">

    <article class="tag tag--holiday">
      <svg class="tag__band" viewBox="0 0 420 472" preserveAspectRatio="none" aria-hidden="true">
        <polygon points="215,0 420,0 420,60 180,472 0,472 0,340"/>
      </svg>
      <div class="brand"><span class="brand__square"></span><span class="brand__name">ZORM Design</span></div>
      <h2 class="item-name"><span>knit</span><span>hat</span></h2>
      <p class="size">One Size</p>
    </article>

    <article class="tag tag--kids">
      <svg class="tag__band" viewBox="0 0 420 472" preserveAspectRatio="none" aria-hidden="true">
        <polygon points="215,0 420,0 420,60 180,472 0,472 0,340"/>
      </svg>
      <div class="brand"><span class="brand__square"></span><span class="brand__name">ZORM Design</span></div>
      <h2 class="item-name"><span>knit</span><span>hat</span></h2>
      <p class="size">One Size</p>
    </article>

    <article class="tag tag--mens">
      <svg class="tag__band" viewBox="0 0 420 472" preserveAspectRatio="none" aria-hidden="true">
        <polygon points="215,0 420,0 420,60 180,472 0,472 0,340"/>
      </svg>
      <div class="brand"><span class="brand__square"></span><span class="brand__name">ZORM Design</span></div>
      <h2 class="item-name"><span>knit</span><span>hat</span></h2>
      <p class="size">One Size</p>
    </article>

    <article class="tag tag--ladies">
      <svg class="tag__band" viewBox="0 0 420 472" preserveAspectRatio="none" aria-hidden="true">
        <polygon points="215,0 420,0 420,60 180,472 0,472 0,340"/>
      </svg>
      <div class="brand"><span class="brand__square"></span><span class="brand__name">ZORM Design</span></div>
      <h2 class="item-name"><span>knit</span><span>hat</span></h2>
      <p class="size">One Size</p>
    </article>

  </main>
</body>
</html>
```